Vellmore Quadrant Systems LLC
Elevate Your Workflow
Vellmore Quadrant Systems LLC - Information Technology
Creative Brief
Corporate
Dorian Feltcher
President
Brenton Falls, VA
dorian@vellmore-quadrant.example
www.vellmore-quadrant.example
Elevate Your Workflow www.vellmore-quadrant.example

```html
<!DOCTYPE html>
<html lang="en">
<head>
<meta charset="utf-8">
<title>Vellmore Quadrant Systems LLC — Business Cards</title>
<link rel="stylesheet" href="https://fonts.googleapis.com/css2?family=Arimo:wght@400;700&display=swap">
<style>
  :root {
    --teal: #3bb4c4;
    --ink: #3d3d3d;
    --card-white: #ffffff;
    --backdrop: #e8e7e3;
  }
  * { box-sizing: border-box; margin: 0; padding: 0; }
  html, body {
    width: 1200px; height: 782px; overflow: hidden;
    background: var(--backdrop);
    font-family: "Arimo", Arial, sans-serif;
  }
  .canvas { position: relative; width: 1200px; height: 782px; }

  .card {
    position: absolute;
    border-radius: 16px;
    box-shadow: 0 4px 14px rgba(0,0,0,.18);
    overflow: hidden;
  }
  .card--front { left: 331px; top: 46px; width: 530px; height: 304px; background: var(--card-white); }
  .card--back-teal { left: 72px; top: 367px; width: 528px; height: 305px; background: var(--teal); }
  .card--back-white { left: 629px; top: 367px; width: 535px; height: 305px; background: var(--card-white); }

  .brand { position: absolute; display: flex; align-items: center; gap: 10px; }
  .brand__mark { width: 30px; height: 30px; background: var(--teal); flex: none; }
  .brand__text { display: flex; flex-direction: column; }
  .brand__name {
    font-weight: 700; font-size: 17px; line-height: 1.15;
    color: var(--ink); letter-spacing: .3px; max-width: 190px;
  }
  .brand__tagline { font-size: 10px; color: var(--ink); margin-top: 3px; }

  .card--front .brand { left: 20px; top: 120px; }
  .card--back-teal .brand { left: 130px; top: 116px; }
  .card--back-teal .brand__mark { background: var(--card-white); }
  .card--back-teal .brand__name,
  .card--back-teal .brand__tagline { color: var(--card-white); }
  .card--back-white .brand { left: 120px; top: 116px; }

  .contact { position: absolute; left: 266px; top: 60px; color: var(--ink); }
  .contact__name { font-weight: 700; font-size: 17px; line-height: 20px; color: var(--teal); }
  .contact__role { font-size: 14px; line-height: 18px; margin-top: 2px; }
  .contact__city { font-size: 14px; line-height: 18px; margin-top: 50px; }
  .contact__lines { margin-top: 15px; font-size: 14px; line-height: 19px; }
  .contact__label { color: var(--teal); font-weight: 700; }

  .card__url {
    position: absolute; left: 0; right: 0; bottom: 25px;
    text-align: center; font-size: 15px;
  }
  .card--back-teal .card__url { color: var(--ink); }
  .card--back-white .card__url { color: var(--teal); }
</style>
</head>
<body>
<main class="canvas">

  <section class="card card--front" aria-label="Business card front">
    <div class="brand">
      <span class="brand__mark"></span>
      <div class="brand__text">
        <span class="brand__name">Vellmore Quadrant Systems LLC</span>
        <span class="brand__tagline">Elevate Your Workflow</span>
      </div>
    </div>
    <div class="contact">
      <p class="contact__name">Dorian Feltcher</p>
      <p class="contact__role">President</p>
      <p class="contact__city">Brenton Falls, VA</p>
      <div class="contact__lines">
        <p><span class="contact__label">C</span> : 202.555.0147</p>
        <p><span class="contact__label">E</span> : dorian@vellmore-quadrant.example</p>
        <p><span class="contact__label">W</span> : www.vellmore-quadrant.example</p>
      </div>
    </div>
  </section>

  <section class="card card--back-teal" aria-label="Business card back, teal">
    <div class="brand">
      <span class="brand__mark"></span>
      <div class="brand__text">
        <span class="brand__name">Vellmore Quadrant Systems LLC</span>
        <span class="brand__tagline">Elevate Your Workflow</span>
      </div>
    </div>
    <p class="card__url">www.vellmore-quadrant.example</p>
  </section>

  <section class="card card--back-white" aria-label="Business card back, white">
    <div class="brand">
      <span class="brand__mark"></span>
      <div class="brand__text">
        <span class="brand__name">Vellmore Quadrant Systems LLC</span>
        <span class="brand__tagline">Elevate Your Workflow</span>
      </div>
    </div>
    <p class="card__url">www.vellmore-quadrant.example</p>
  </section>

</main>
</body>
</html>
```